CD Cover Design Project - Marisa Penhallow

We need an ablum / cd cover design for the artist Marisa Penhallow - www.marisapenhallow.com

The album is called "Quiet Rooms At Dusk"

General
A ‘Quiet Rooms’ is a very traditional and formal art form. With this in mind, the artwork should have an ‘old’ feel, for lack of a better word. I don’t envision anything too contemporary or clean., I imagine something like an old letter or photograph, yellow round the edges and somehow nostalgic.

Colour scheme
This should not be too saturated with colour, but not devoid of it either. I’m a fan of colour – it definitely needs to be in there! We just need to base it on the main image, derive the colour palette from there and reference it constantly.

Font
In keeping with the idea of an old letter, this should be something like an old feather quill and ink, if possible. Can this be hand-written???

Reverse of CD:

Track Listing

MERIDEN
Penhallow, Haldecott

BALLAST
Penhallow

BLUE TIMBER
Penhallow

ONCE WE’RE GONE
Penhallow, Haldecott

PAPER HARBOUR
Penhallow, Haldecott

WINTER SPARROW
Penhallow, Pryce

TURNING THE KEY
Ardley/Vantreece

BY THE LOW BRIDGE
Penhallow

SALT IN POCKET
Penhallow, Dunmore

OSTEND
Penhallow, Penhallow

Quiet Rooms produced by Marisa Penhallow, Owen Palliser, Tom Reddaway & Luke Farrant

All tracks except Ostend recorded first at Quarry Lane Rooms London with Stephen Mabery, then engineered and produced by Owen Palliser at Venbrook, then final production and finishing touches at Pelican Yard Studios with Tom Reddaway & Luke Farrant. Ostend was recorded at xxxx with Harold Quistmann and finished at Pelican Yard Studios with Tom Reddaway & Luke Farrant.

Barcode (dummy please)

Management BrightSpan ltd - admin@brightspan.ltd.uk 0207 946 0352

©BrightSpan Publishing 2013. All rights reserverd. Unauthorised
copying, reproduction, hiring, public performance and broadcasting prohibited. www.brightspan.ltd.uk

Requirements
Must have
• You need to use this image on the cover:

https://www.filevaultix.com/s/k7tr2mpq9wze81c/Marisa-QuietRooms_Cover.tif

I have uploaded the jpg but this is better quality.

```html
<!DOCTYPE html>
<html lang="en">
<head>
<meta charset="utf-8">
<title>Quiet Rooms At Dusk – Marisa Penhallow</title>
<link rel="stylesheet" href="https://fonts.googleapis.com/css2?family=Yellowtail&family=Kaushan+Script&display=swap">
<style>
  :root {
    --page: #ffffff;
    --paper-light: #d9b876;
    --paper-mid: #c29a55;
    --paper-dark: #7d5a28;
    --ink: #17110a;
    --torn: #fdfcf8;
  }
  * { margin: 0; padding: 0; box-sizing: border-box; }
  html, body {
    width: 1200px; height: 900px; overflow: hidden;
    background: var(--page);
  }
  .cover {
    position: absolute; left: 170px; top: 20px;
    width: 860px; height: 860px;
    background: var(--torn);
    color: var(--ink);
    font-family: "Yellowtail", cursive;
  }
  .cover__paper { position: absolute; inset: 0; width: 100%; height: 100%; }
  .cover__title {
    position: absolute; left: 230px; top: 100px;
    font-family: "Kaushan Script", cursive;
    line-height: 1;
  }
  .cover__title-line { display: block; }
  .cover__title-line--top { font-size: 50px; }
  .cover__title-line--bottom { font-size: 84px; margin: 4px 0 0 60px; }
  .track { position: absolute; line-height: 1; }
  .track__name { display: block; font-size: 36px; }
  .track__credit {
    display: block; font-size: 12px;
    font-family: "Kaushan Script", cursive;
    margin-top: -2px;
  }
  .track--left { text-align: left; }
  .track--left .track__credit { padding-left: 86px; }
  .track--right { text-align: right; }
  .track--right .track__credit { padding-right: 60px; }
  .cover__artist {
    position: absolute; right: 30px; bottom: 26px;
    font-family: "Kaushan Script", cursive;
    font-size: 40px; line-height: 0.85; text-align: right;
  }
  .cover__artist span { display: block; }
</style>
</head>
<body>
  <main class="cover">
    <svg class="cover__paper" viewBox="0 0 860 860" role="img" aria-label="Aged, torn parchment sheet with ink splatter running across it">
      <defs>
        <radialGradient id="parchment" cx="50%" cy="45%" r="70%">
          <stop offset="0" stop-color="var(--paper-light)"/>
          <stop offset="0.65" stop-color="var(--paper-mid)"/>
          <stop offset="1" stop-color="var(--paper-dark)"/>
        </radialGradient>
      </defs>
      <path d="M0 0 H860 V600 C820 650 790 640 760 700 C730 760 680 790 630 860 H0 Z" fill="url(#parchment)"/>
    </svg>

    <h1 class="cover__title">
      <span class="cover__title-line cover__title-line--top">Quiet Rooms</span>
      <span class="cover__title-line cover__title-line--bottom">At Dusk</span>
    </h1>

    <ol class="tracklist">
      <li class="track track--left" style="left:44px; top:300px;"><span class="track__name">Meriden</span><span class="track__credit">Penhallow, Haldecott</span></li>
      <li class="track track--left" style="left:26px; top:400px;"><span class="track__name">Ballast</span><span class="track__credit">Penhallow</span></li>
      <li class="track track--left" style="left:26px; top:492px;"><span class="track__name">Blue Timber</span><span class="track__credit">Penhallow</span></li>
      <li class="track track--left" style="left:64px; top:586px;"><span class="track__name">Once We’re Gone</span><span class="track__credit">Penhallow, Haldecott</span></li>
      <li class="track track--left" style="left:140px; top:700px;"><span class="track__name">Paper Harbour</span><span class="track__credit">Penhallow, Haldecott</span></li>

      <li class="track track--right" style="right:36px; top:312px;"><span class="track__name">Winter Sparrow</span><span class="track__credit">Penhallow, Pryce</span></li>
      <li class="track track--right" style="right:40px; top:405px;"><span class="track__name">Turning the Key</span><span class="track__credit">Ardley / Vantreece</span></li>
      <li class="track track--right" style="right:16px; top:498px;"><span class="track__name">By the Low Bridge</span><span class="track__credit">Penhallow</span></li>
      <li class="track track--right" style="right:90px; top:590px;"><span class="track__name">Salt in Pocket</span><span class="track__credit">Penhallow, Dunmore</span></li>
      <li class="track track--left" style="left:498px; top:712px;"><span class="track__name">Ostend</span><span class="track__credit" style="padding-left:10px;">Penhallow</span></li>
    </ol>

    <p class="cover__artist"><span>Marisa</span><span>Penhallow</span></p>
  </main>
</body>
</html>
```